Beer can label design for 12oz cans

we want a clean easy to read label we will be changing the colors to coordinate with the name change of the beer but want everyone to know what they are looking at in regards to the type of beer and us as a brewery. we are in Alaska and i picture a orange red blue green and maybe yellow color to make it clear what beer they are buying. it will be going on a 12oz can. wold like the logo to be 1 color like a dark grey maybe a weatherd look at angle maybe just to give it a little character. needs to have PINE HOLLOW, AK on the top or the label also needs to have made in alaska somewhere on there. there are lots of rules here are some designs i reallylike also. we are on a lake and look at north americas tallest mountain, Denali Moutain.

Target Market(s)

beer drinkers, want a recognizable can thats easy to decipher the beer type

Industry/Entity Type

drink branding.

Requirements
Must have
• this will be call the "Cold Ox" its a double IPA needs to have the appropriate letter sizes and requirements for a label
Nice to have
• want it to be clean but pop also

```html
<!DOCTYPE html>
<html lang="en">
<head>
<meta charset="utf-8">
<title>Kestrel Brewing – Cold Ox Double IPA label</title>
<link href="https://fonts.googleapis.com/css2?family=Montserrat:wght@300;400;500;800;900&family=Roboto:wght@400;700&display=swap" rel="stylesheet">
<style>
  :root{
    --page:#ffffff;
    --sky-top:#b9d9ea;
    --sky-bottom:#d6e8f2;
    --ink-dark:#2e2c2e;
    --snow:#f3f6f8;
    --ridge:#9fbccd;
    --forest:#2b4665;
    --forest-deep:#1f3352;
    --band-blue:#3f8bc4;
    --band-light:#6db3e0;
    --navy-type:#2a3f5f;
    --white:#ffffff;
  }
  *{margin:0;padding:0;box-sizing:border-box}
  html,body{width:1200px;height:1200px;overflow:hidden;background:var(--page)}
  .canvas{position:relative;width:1200px;height:1200px}
  .label{
    position:absolute;left:260px;top:45px;width:680px;height:1110px;
    overflow:hidden;
    background:linear-gradient(180deg,var(--sky-top) 0%,var(--sky-bottom) 40%);
  }
  .location{
    position:absolute;top:80px;left:0;width:100%;text-align:center;
    font-family:'Montserrat',sans-serif;font-weight:500;font-size:40px;
    letter-spacing:7px;color:var(--ink-dark);
  }
  .brewery{
    position:absolute;top:160px;left:0;width:100%;text-align:center;
    font-family:'Montserrat',sans-serif;font-weight:900;color:var(--ink-dark);
    line-height:1;
  }
  .brewery .name{display:block;font-size:112px;letter-spacing:-2px}
  .brewery .sub{display:block;font-size:44px;letter-spacing:6px;margin-top:8px}
  .scene{
    position:absolute;left:0;top:380px;width:100%;height:365px;
  }
  .scene svg{display:block;width:100%;height:100%}
  .made-in{
    position:absolute;top:663px;left:0;width:100%;text-align:center;
    font-family:'Roboto',sans-serif;font-weight:700;font-size:44px;
    letter-spacing:5px;color:var(--white);
  }
  .beer-band{
    position:absolute;left:0;top:745px;width:100%;height:365px;
    background:linear-gradient(90deg,var(--band-blue) 0%,var(--band-light) 25%,#2f6fa6 55%,var(--band-blue) 85%,#5aa5dd 100%);
    text-align:center;
  }
  .beer-name{
    margin-top:22px;font-family:'Montserrat',sans-serif;font-weight:900;
    font-size:118px;line-height:1;color:var(--white);letter-spacing:1px;
  }
  .beer-style{
    margin-top:6px;font-family:'Montserrat',sans-serif;font-size:70px;line-height:1;
    color:var(--navy-type);
  }
  .beer-style .light{font-weight:300}
  .beer-style .bold{font-weight:800}
  .beer-facts{
    margin-top:26px;font-family:'Roboto',sans-serif;font-weight:400;
    font-size:30px;line-height:1.35;color:var(--white);letter-spacing:1px;
  }
</style>
</head>
<body>
<div class="canvas">
  <div class="label">
    <div class="location">PINE HOLLOW, AK</div>
    <div class="brewery">
      <span class="name">KESTREL</span>
      <span class="sub">BREWING</span>
    </div>
    <div class="scene" role="img" aria-label="Illustration of a snow-capped mountain behind a dark spruce forest">
      <svg viewBox="0 0 680 365" preserveAspectRatio="none">
        <defs>
          <linearGradient id="sceneTone" x1="0" y1="0" x2="0" y2="1">
            <stop offset="0" stop-color="var(--snow)"/>
            <stop offset="0.35" stop-color="var(--ridge)"/>
            <stop offset="0.6" stop-color="var(--forest)"/>
            <stop offset="1" stop-color="var(--forest-deep)"/>
          </linearGradient>
        </defs>
        <rect width="680" height="365" fill="url(#sceneTone)"/>
      </svg>
    </div>
    <div class="made-in">Made in Alaska</div>
    <div class="beer-band">
      <div class="beer-name">COLD OX</div>
      <div class="beer-style"><span class="light">DOUBLE</span> <span class="bold">IPA</span></div>
      <div class="beer-facts">6.2% ALC. BY VOL. | 50 IBU<br>CONTENTS 12 FL.OZ</div>
    </div>
  </div>
</div>
</body>
</html>
```